Kestrel Signs Facebook Banner Design

Design a facebook banner for a sign company. I would like to have a modern approach to it.

Product Offering:
Signs
Banners
Decals
Commercial Wraps

```html
<!DOCTYPE html>
<html lang="en">
<head>
<meta charset="utf-8">
<title>Kestrel Signs – Facebook Cover</title>
<link rel="stylesheet" href="https://fonts.googleapis.com/css2?family=Poppins:ital,wght@0,300;1,400&family=Roboto:wght@500&family=Saira+Condensed:ital,wght@0,800;1,700&display=swap">
<style>
  :root {
    --stage: #5f6a70;
    --white: #ffffff;
    --red: #e8303a;
    --red-deep: #a81e25;
    --charcoal: #3a3a3c;
    --charcoal-dark: #262628;
    --silver: #d9d9d9;
    --ink: #111111;
    --strip: #e9e9e9;
    --frame: #d2d2d2;
    --page-name: #555555;
  }
  html, body {
    margin: 0;
    width: 1200px;
    height: 1200px;
    overflow: hidden;
    background: var(--stage);
  }
  .page-preview {
    position: absolute;
    left: 109px;
    top: 394px;
    width: 981px;
    height: 425px;
    box-shadow: 0 18px 30px rgba(0,0,0,.35);
  }
  .page-preview svg { display: block; width: 100%; height: 100%; }
  .welcome { font-family: "Poppins", sans-serif; font-style: italic; font-weight: 400; font-size: 25px; fill: var(--ink); }
  .welcome-name { font-family: "Poppins", sans-serif; font-weight: 300; font-size: 36px; fill: var(--white); }
  .headline, .service {
    font-family: "Saira Condensed", sans-serif;
    font-style: italic;
    font-weight: 700;
    fill: var(--white);
  }
  .headline { font-size: 80px; }
  .service { font-size: 64px; }
  .brand-name {
    font-family: "Saira Condensed", sans-serif;
    font-weight: 800;
    fill: var(--charcoal);
  }
  .brand-name--panel { font-size: 44px; }
  .brand-name--avatar { font-size: 32px; }
  .page-name { font-family: "Roboto", sans-serif; font-weight: 500; font-size: 30px; fill: var(--page-name); }
</style>
</head>
<body>
<div class="page-preview">
  <svg viewBox="0 0 1580 684" xmlns="http://www.w3.org/2000/svg">
    <defs>
      <linearGradient id="silverPanel" x1="0" y1="0" x2="1" y2="0">
        <stop offset="0" stop-color="var(--silver)"/>
        <stop offset="0.35" stop-color="var(--white)"/>
      </linearGradient>
      <linearGradient id="redTile" x1="0" y1="0" x2="0" y2="1">
        <stop offset="0" stop-color="var(--red)"/>
        <stop offset="1" stop-color="var(--red-deep)"/>
      </linearGradient>
      <linearGradient id="darkBand" x1="0" y1="0" x2="1" y2="0">
        <stop offset="0" stop-color="var(--charcoal)"/>
        <stop offset="1" stop-color="var(--charcoal-dark)"/>
      </linearGradient>
      <linearGradient id="photoTones" x1="0" y1="0" x2="1" y2="1">
        <stop offset="0" stop-color="#2b6f8a"/>
        <stop offset="0.45" stop-color="#5aa9b8"/>
        <stop offset="0.7" stop-color="#c9a24a"/>
        <stop offset="1" stop-color="#3b8f6a"/>
      </linearGradient>
    </defs>

    <!-- cover -->
    <rect class="cover" width="1580" height="588" fill="var(--white)"/>

    <!-- brand panel -->
    <polygon class="brand-panel" points="508,0 915,0 790,270 655,270" fill="url(#silverPanel)"/>
    <polygon class="accent-line" points="495,0 505,0 650,275 640,275" fill="var(--red)"/>
    <text class="brand-name brand-name--panel" x="717" y="114" text-anchor="middle">KESTREL</text>
    <text class="brand-name brand-name--panel" x="717" y="152" text-anchor="middle">SIGNS</text>

    <!-- photo area -->
    <g role="img" aria-label="Photo of a screen printer lifting a print frame in a workshop with shelves of coloured inks">
      <polygon points="940,0 1580,0 1580,292 803,292" fill="url(#photoTones)"/>
    </g>

    <!-- divider stripe -->
    <polygon class="divider" points="915,0 937,0 615,588 587,588" fill="var(--charcoal)"/>

    <!-- service tiles -->
    <polygon class="tile-row" points="775,297 1580,297 1580,418 710,418" fill="url(#redTile)"/>
    <polygon class="tile-row" points="708,422 1580,422 1580,588 617,588" fill="url(#redTile)"/>
    <polygon class="tile-edge" points="775,297 800,297 735,418 710,418" fill="var(--red-deep)"/>
    <polygon class="tile-edge" points="708,422 730,422 642,588 617,588" fill="var(--red-deep)"/>
    <polygon class="tile-split" points="1130,297 1148,297 1093,418 1075,418" fill="var(--red-deep)"/>
    <polygon class="tile-split" points="1068,422 1088,422 1020,588 1000,588" fill="var(--red-deep)"/>

    <text class="service" x="867" y="379" textLength="146" lengthAdjust="spacingAndGlyphs">SIGNS</text>
    <text class="service" x="1185" y="379" textLength="225" lengthAdjust="spacingAndGlyphs">BANNERS</text>
    <text class="service" x="813" y="496" textLength="177" lengthAdjust="spacingAndGlyphs">DECALS</text>
    <text class="service" x="1120" y="496" textLength="317" lengthAdjust="spacingAndGlyphs">COMMERCIAL</text>
    <text class="service" x="1122" y="552" textLength="171" lengthAdjust="spacingAndGlyphs">WRAPS</text>

    <!-- welcome tag -->
    <text class="welcome" x="77" y="73" textLength="168" lengthAdjust="spacingAndGlyphs">Welcome To</text>
    <polygon class="name-tag" points="47,92 420,92 447,142 72,142" fill="var(--red)"/>
    <polygon class="name-tag-stripe" points="425,92 455,92 482,142 452,142" fill="var(--charcoal)"/>
    <text class="welcome-name" x="77" y="128" textLength="285" lengthAdjust="spacingAndGlyphs">Kestrel Signs</text>

    <!-- headline bands -->
    <polygon class="headline-band" points="0,173 583,173 645,275 0,275" fill="var(--red)"/>
    <text class="headline" x="62" y="259" textLength="503" lengthAdjust="spacingAndGlyphs">TOP SIGN DESIGN</text>
    <polygon class="headline-band" points="0,277 730,277 680,379 0,379" fill="url(#darkBand)"/>
    <text class="headline" x="58" y="356" textLength="615" lengthAdjust="spacingAndGlyphs">&amp; PRINTING EXPERTS</text>

    <!-- profile strip -->
    <rect class="profile-strip" x="0" y="588" width="1580" height="96" fill="var(--strip)"/>
    <rect class="profile-avatar" x="59.5" y="449.5" width="202" height="202" fill="var(--white)" stroke="var(--frame)" stroke-width="3"/>
    <text class="brand-name brand-name--avatar" x="160" y="554" text-anchor="middle">KESTREL</text>
    <text class="brand-name brand-name--avatar" x="160" y="582" text-anchor="middle">SIGNS</text>
    <text class="page-name" x="310" y="640">Kestrel Signs</text>
  </svg>
</div>
</body>
</html>
```